QPM Habitat Helpers 2019

We need a 2 page flyer to advertise our upcoming program. The program covers 5 months May-September 2019 and is focused on conservation.I have attached some options that i like. It needs to be striking.

Text in newly uploaded document 'HHFlyer2'

Target Market(s)

Conservation
Conscious travelers
30-45 year olds
Environmental
Adventure/Hiking
Citizen Science

Font styles to use
Sans Serif

Colors
0355a3
fbed22

Requirements
Must have
• A travel conservation focus
• Highlight the significance of the 'in the world' status of the project
Nice to have
• A yellow border, making it look similar to the cover of Wandering Horizons

```html
<!DOCTYPE html>
<html lang="en">
<head>
<meta charset="utf-8">
<title>Habitat Helpers 2019 – Flyer</title>
<link href="https://fonts.googleapis.com/css2?family=Oswald:wght@500;700&family=Open+Sans:wght@400;600;700&display=swap" rel="stylesheet">
<style>
  :root {
    --brand-blue: #0355a3;
    --brand-yellow: #fbed22;
    --band-blue: #a9c8e6;
    --band-blue-light: #cfe0f1;
    --ink: #1d3557;
    --paper: #ffffff;
    --backdrop: #6f4a8e;
    --photo-sky: #9cc3dc;
    --photo-sea: #2f6f97;
    --photo-land: #3e5b3a;
  }
  * { box-sizing: border-box; margin: 0; padding: 0; }
  html, body { width: 1200px; height: 960px; overflow: hidden; }
  body {
    background: var(--backdrop);
    font-family: "Open Sans", Arial, sans-serif;
    display: flex;
    align-items: center;
    justify-content: center;
    gap: 40px;
  }
  .page {
    width: 560px;
    height: 792px;
    background: var(--paper);
    position: relative;
    overflow: hidden;
    box-shadow: 0 10px 30px rgba(0,0,0,.25);
  }

  /* ---------- Page one: cover ---------- */
  .cover-hero {
    position: relative;
    height: 330px;
    background: linear-gradient(180deg, var(--photo-sky) 0%, #c9dde9 38%, var(--photo-sea) 55%, #4d7a93 70%, var(--photo-land) 100%);
  }
  .cover-hero .frame-line {
    position: absolute;
    top: 30px;
    bottom: 60px;
    width: 3px;
    background: var(--brand-yellow);
  }
  .cover-hero .frame-line.left { left: 330px; }
  .cover-hero .frame-line.right { left: 470px; }
  .cover-headline {
    position: absolute;
    left: 28px;
    right: 28px;
    bottom: 22px;
    font-family: "Oswald", "Arial Narrow", sans-serif;
    font-weight: 700;
    font-size: 40px;
    letter-spacing: .5px;
    color: var(--paper);
    text-transform: uppercase;
    line-height: 1;
  }
  .cover-body {
    padding: 22px 46px 0;
    text-align: center;
    color: var(--ink);
    font-size: 12px;
    line-height: 1.55;
  }
  .cover-body p + p { margin-top: 10px; }
  .org-mark {
    display: flex;
    align-items: center;
    justify-content: center;
    gap: 8px;
    margin: 16px 0 14px;
    color: var(--brand-blue);
    font-weight: 700;
    font-size: 13px;
  }
  .org-mark .dot {
    width: 22px; height: 22px;
    border-radius: 50%;
    border: 2px solid var(--brand-blue);
  }
  .activity-strip {
    margin: 0 24px;
    background: var(--brand-blue);
    color: var(--paper);
    text-align: center;
    font-family: "Oswald", "Arial Narrow", sans-serif;
    font-weight: 500;
    font-size: 14px;
    letter-spacing: .5px;
    text-transform: uppercase;
    padding: 6px 0;
  }
  .activities {
    display: grid;
    grid-template-columns: repeat(4, 1fr);
    gap: 8px;
    margin: 8px 24px 0;
  }
  .activity .shot { height: 86px; }
  .shot.planting { background: linear-gradient(160deg, #6f9a5a, #31502c); }
  .shot.seabirds { background: linear-gradient(170deg, #9dc2dc, #3f6f8f); }
  .shot.trails { background: linear-gradient(170deg, #a8c6a0, #3a5c38); }
  .shot.reef { background: linear-gradient(170deg, #7fc7cf, #2f7f98); }
  .activity p {
    margin-top: 6px;
    font-size: 10.5px;
    line-height: 1.4;
    color: var(--ink);
  }

  /* ---------- Page two: values ---------- */
  .values {
    position: absolute;
    top: 30px;
    left: 30px;
    right: 30px;
    display: flex;
    flex-direction: column;
    gap: 12px;
  }
  .value-band {
    height: 68px;
    background: var(--band-blue-light);
    display: flex;
    align-items: center;
    color: var(--paper);
    font-size: 28px;
    font-weight: 600;
    padding-left: 150px;
    text-shadow: 0 0 1px rgba(3,85,163,.4);
  }
  .value-band:nth-child(odd) {
    background: var(--band-blue);
    padding-left: 200px;
  }
  .protect-bar {
    position: absolute;
    top: 0;
    bottom: 90px;
    left: 120px;
    width: 44px;
    background: var(--brand-yellow);
    display: flex;
    align-items: center;
    justify-content: center;
  }
  .protect-bar span {
    writing-mode: vertical-rl;
    text-orientation: upright;
    font-family: "Oswald", "Arial Narrow", sans-serif;
    font-weight: 700;
    font-size: 46px;
    color: var(--brand-blue);
    letter-spacing: 4px;
    line-height: 1;
  }
  .partner-footer {
    position: absolute;
    left: 0; right: 0; bottom: 0;
    height: 90px;
    background: var(--paper);
    border-top: 4px solid var(--brand-yellow);
    display: flex;
    flex-direction: column;
    align-items: center;
    justify-content: center;
    gap: 10px;
  }
  .partners { display: flex; gap: 16px; align-items: center; }
  .partner-badge { width: 34px; height: 22px; background: #c9d6e4; }
  .partner-badge.round { width: 24px; height: 24px; border-radius: 50%; }
  .apply-line { font-size: 11px; font-weight: 600; color: var(--brand-blue); }
</style>
</head>
<body>

  <section class="page cover">
    <div class="cover-hero" role="img" aria-label="Photo of a hiker standing on a mountain ridge above a blue lagoon and ocean">
      <span class="frame-line left"></span>
      <span class="frame-line right"></span>
      <h1 class="cover-headline">Make a difference in 2019</h1>
    </div>
    <div class="cover-body">
      <p>Join a hands-on conservation season on a World Heritage island, one of the few places in the world where rare species still thrive.</p>
      <p>From May to September 2019 our volunteers restore habitat, track wildlife and support citizen science alongside local rangers.</p>
    </div>
    <div class="org-mark"><span class="dot"></span>QPM Habitat Helpers</div>
    <div class="activity-strip">Five months. One island. Lasting impact.</div>
    <div class="activities">
      <div class="activity">
        <div class="shot planting" role="img" aria-label="Photo of volunteers planting native seedlings"></div>
        <p>Plant native seedlings across restoration sites</p>
      </div>
      <div class="activity">
        <div class="shot seabirds" role="img" aria-label="Photo of seabirds on coastal cliffs"></div>
        <p>Survey seabirds along the coastal cliffs</p>
      </div>
      <div class="activity">
        <div class="shot trails" role="img" aria-label="Photo of a mountain trail through forest"></div>
        <p>Hike remote trails to record rare plants</p>
      </div>
      <div class="activity">
        <div class="shot reef" role="img" aria-label="Photo of a snorkeller over a coral reef"></div>
        <p>Monitor reef health with the marine team</p>
      </div>
    </div>
  </section>

  <section class="page values-page">
    <div class="values">
      <div class="value-band">Paradise</div>
      <div class="value-band">Conservation</div>
      <div class="value-band">World Heritage</div>
      <div class="value-band">Adventure</div>
      <div class="value-band">Volunteers</div>
      <div class="value-band">Citizen Science</div>
      <div class="value-band">One in the World</div>
      <div class="value-band">Restoration</div>
    </div>
    <div class="protect-bar"><span>PROTECT</span></div>
    <footer class="partner-footer">
      <div class="partners">
        <span class="partner-badge round"></span>
        <span class="partner-badge"></span>
        <span class="partner-badge round"></span>
        <span class="partner-badge"></span>
        <span class="partner-badge"></span>
        <span class="partner-badge round"></span>
        <span class="partner-badge"></span>
      </div>
      <p class="apply-line">Apply now at islandhelpers-season.net</p>
    </footer>
  </section>

</body>
</html>
```